TALLVEX MOTOR OIL LABEL

I am launching a new motor oil product called TallVex and I would like your help in designing the packaging. The product is aimed at delivering high-performance results for vehicles, and I want the packaging to reflect the premium quality and reliability of TallVex. The design should be modern, dynamic, and appeal to car enthusiasts, while also communicating trust and innovation. I’m looking for a sleek and professional look that stands out on the shelf. Please incorporate elements that highlight its efficiency and performance, with bold typography and striking colors to grab attention.
I also need a logo for the name TallVex, and I would like your help in choosing the right colors for the packaging. The logo should be bold, memorable, and represent the strength and high performance of the product. When it comes to the packaging colors, I want something that is both eye-catching and conveys a sense of power and reliability, while also appealing to car enthusiasts. Your guidance in selecting the perfect color scheme to match the brand identity will be greatly appreciated.
The types of oils I plan to offer are available in the following sizes: 1 liter, 4 liters, and 5 liters.

• 10W40 Synthetic Blend High Mileage
• 20W50 Synthetic Blend High Mileage
• 10W30 Synthetic Blend High Mileage
• 5W30 Synthetic Blend High Mileage
• 5W20 Synthetic Blend High Mileage

Additionally, I will offer

Additionally, I will offer a
0W16 FULL SYNTHETIC
OW20 FULL SYNTHETIC
5W20 FULL SYNTHETIC
5W30 FULL SYNTHETIC
5W40 FULL SYNTHETIC
0W40 FULL SYNTHETIC
AND HD MOTOR OIL
15W40 HAVEY DUTY DIESEL ENGINE OIL SYNTHETIC BLEND
5W40 HAVEY DUTY DIESEL ENGINE OIL FULL SYNTHETIC

Font styles to use
Serif

Colors
0054AA
0677BA
7BADD7
CADEEF
E8F1F8
59FF00
82FF00
B8FF75
E3FFCB
F4FFEA
FFF300
FFF600
FEFA6F
FFFEC7
FFFEE8
FFC000
F8CF3A
FAE287
FDF2CF
FEFAEE
F0912C
F2A743
F7CA91
FBE8D2
FDF5EE
EB3D1F
EC4F4E
F09395
F8D3D4
FCEDEE

```html
<!DOCTYPE html>
<html lang="en">
<head>
<meta charset="utf-8">
<title>TallVex Motor Oil – Label Range</title>
<link href="https://fonts.googleapis.com/css2?family=Oswald:wght@700&family=Roboto+Condensed:wght@400;700;900&display=swap" rel="stylesheet">
<style>
  :root {
    --canvas: #ffffff;
    --label-black: #050505;
    --brand-cream: #fde6b0;
    --oil-orange: #f5a21e;
    --art-orange: #f2a743;
    --art-yellow: #f8cf3a;
    --cyan-light: #5fd3f5;
    --cyan-mid: #2aa6d6;
    --blue-deep: #1e5bb8;
    --blue-bar: #2a63c6;
    --blue-soft: #6b97d8;
    --grade-badge: #1b8fbf;
    --text-white: #ffffff;
    --tagline-cyan: #2fa0cc;
    --gold-line: #c99a45;
  }
  * { margin: 0; padding: 0; box-sizing: border-box; }
  html, body { width: 1200px; height: 927px; overflow: hidden; background: var(--canvas); }
  .label-range {
    position: relative;
    width: 1200px; height: 927px;
    display: flex; align-items: flex-end; justify-content: center;
    gap: 70px; padding-bottom: 170px;
  }
  .label { display: block; }
  .label--5l, .label--4l { width: 340px; height: 489px; }
  .label--1l { width: 240px; height: 340px; }

  .bg { fill: var(--label-black); }
  .band-blue { fill: var(--blue-deep); }
  .bar-blue { fill: var(--blue-bar); }
  .bar-soft { fill: var(--blue-soft); }
  .band-cyan { fill: url(#cyanBand); }
  .line-orange { stroke: var(--oil-orange); stroke-width: 5; }
  .line-gold { stroke: var(--gold-line); stroke-width: 2.5; }
  .art-area { fill: url(#artFill); }

  .t-perf { font-family: "Roboto Condensed", sans-serif; font-weight: 400; fill: var(--text-white); letter-spacing: 1px; }
  .t-brand { font-family: "Oswald", sans-serif; font-weight: 700; fill: var(--brand-cream); }
  .t-motor { font-family: "Roboto Condensed", sans-serif; font-weight: 900; fill: var(--oil-orange); letter-spacing: 1px; }
  .t-tag { font-family: "Roboto Condensed", sans-serif; font-weight: 400; fill: var(--tagline-cyan); }
  .t-full { font-family: "Roboto Condensed", sans-serif; font-weight: 900; fill: var(--text-white); letter-spacing: 1px; }
  .t-grade { font-family: "Oswald", sans-serif; font-weight: 700; fill: var(--text-white); }
  .grade-badge { fill: var(--grade-badge); }
  .t-volume { font-family: "Roboto Condensed", sans-serif; font-weight: 400; fill: var(--oil-orange); }
  .t-motor-small { font-family: "Roboto Condensed", sans-serif; font-weight: 900; fill: var(--text-white); }
  .t-perf-gold { font-family: "Roboto Condensed", sans-serif; font-weight: 400; fill: var(--oil-orange); }
</style>
</head>
<body>
<svg width="0" height="0" style="position:absolute" aria-hidden="true">
  <defs>
    <linearGradient id="cyanBand" x1="0" y1="0" x2="0" y2="1">
      <stop offset="0" stop-color="#5fd3f5"/>
      <stop offset="1" stop-color="#2aa6d6"/>
    </linearGradient>
    <linearGradient id="artFill" x1="0" y1="0" x2="1" y2="1">
      <stop offset="0" stop-color="#f8cf3a"/>
      <stop offset="1" stop-color="#f2a743"/>
    </linearGradient>
  </defs>
</svg>

<main class="label-range">

  <svg class="label label--5l" viewBox="0 0 410 590" role="group" aria-label="TallVex 10W30 5 litre label">
    <rect class="bg" width="410" height="590"/>
    <polygon class="band-blue" points="170,75 410,15 410,55 170,115"/>
    <g class="bar-blue">
      <polygon points="4,112 14,110 10,155 0,157"/>
      <polygon points="22,108 36,105 32,150 18,153"/>
      <polygon points="46,102 60,99 56,144 42,147"/>
      <polygon points="70,97 84,94 80,139 66,142"/>
      <polygon points="94,92 108,89 104,134 90,137"/>
      <polygon points="118,86 132,83 128,128 114,131"/>
      <polygon points="142,80 156,77 152,122 138,125"/>
    </g>
    <polygon class="band-cyan" points="0,178 410,90 410,145 0,225"/>
    <polygon class="bg" points="0,202 160,168 0,214"/>
    <text class="t-perf" font-size="25" transform="translate(88,205) rotate(-12)">HIGH-PERFORMANCE</text>
    <text class="t-brand" font-size="92" transform="translate(32,330) rotate(-12)">TALLVEX</text>
    <text class="t-motor" font-size="46" transform="translate(98,372) rotate(-12)">MOTOR OIL</text>
    <text class="t-tag" font-size="25" transform="translate(14,420) rotate(-12)">Synthetic Blend High Mileage</text>
    <text class="t-full" font-size="36" transform="translate(32,456) rotate(-12)">FULL SYNTHETIC</text>
    <rect class="art-area" x="125" y="468" width="150" height="80" rx="6" role="img" aria-label="Orange flame swoosh artwork"/>
    <g class="bar-blue">
      <polygon points="296,455 306,452 300,490 290,493"/>
      <polygon points="318,448 330,445 324,483 312,486"/>
      <polygon points="342,440 356,436 350,475 336,478"/>
    </g>
    <polygon class="band-blue" points="370,432 410,420 410,455 362,470"/>
    <rect class="grade-badge" x="14" y="540" width="94" height="38" rx="3"/>
    <text class="t-grade" font-size="28" x="22" y="570">10W30</text>
    <text class="t-volume" font-size="30" x="300" y="570">5Liters</text>
  </svg>

  <svg class="label label--4l" viewBox="0 0 410 590" role="group" aria-label="TallVex 20W50 4 litre label">
    <rect class="bg" width="410" height="590"/>
    <polygon class="band-cyan" points="0,95 410,5 410,20 0,110"/>
    <polygon class="band-cyan" points="0,150 410,60 410,120 0,210"/>
    <polygon class="bg" points="0,178 180,140 0,190"/>
    <text class="t-perf" font-size="25" transform="translate(90,175) rotate(-12)">HIGH-PERFORMANCE</text>
    <text class="t-brand" font-size="92" transform="translate(22,320) rotate(-12)">TALLVEX</text>
    <line class="line-orange" x1="0" y1="348" x2="150" y2="318"/>
    <line class="line-orange" x1="0" y1="362" x2="150" y2="332"/>
    <line class="line-orange" x1="0" y1="376" x2="150" y2="346"/>
    <text class="t-motor" font-size="46" transform="translate(152,348) rotate(-12)">MOTOR OIL</text>
    <text class="t-tag" font-size="29" transform="translate(8,425) rotate(-12)">Synthetic Blend High Mileage</text>
    <text class="t-full" font-size="36" transform="translate(48,458) rotate(-12)">FULL SYNTHETIC</text>
    <rect class="art-area" x="120" y="470" width="130" height="78" rx="6" role="img" aria-label="Orange flame swoosh artwork"/>
    <g class="bar-blue">
      <polygon points="262,520 270,518 270,540 262,542"/>
      <polygon points="278,515 286,513 286,537 278,539"/>
      <polygon points="294,510 302,508 302,534 294,536"/>
      <polygon points="310,505 318,503 318,531 310,533"/>
      <polygon points="326,500 334,498 334,528 326,530"/>
      <polygon points="342,495 350,493 350,525 342,527"/>
    </g>
    <polygon class="bar-soft" points="370,488 410,476 410,502 370,514"/>
    <rect class="grade-badge" x="8" y="545" width="100" height="38" rx="3"/>
    <text class="t-grade" font-size="28" x="16" y="575">20W50</text>
    <text class="t-volume" font-size="30" x="298" y="575">4Liters</text>
  </svg>

  <svg class="label label--1l" viewBox="0 0 265 375" role="group" aria-label="TallVex 10W40 1 litre label">
    <rect class="bg" width="265" height="375"/>
    <text class="t-brand" font-size="62" transform="translate(14,128) rotate(-12)">TALLVEX</text>
    <line class="line-gold" x1="5" y1="160" x2="95" y2="142"/>
    <text class="t-motor-small" font-size="17" transform="translate(96,146) rotate(-12)">MOTOR OIL</text>
    <line class="line-gold" x1="192" y1="112" x2="265" y2="98"/>
    <g class="bar-blue">
      <rect x="188" y="118" width="7" height="16"/>
      <rect x="202" y="115" width="7" height="16"/>
      <rect x="216" y="112" width="7" height="16"/>
      <rect x="230" y="109" width="7" height="16"/>
      <rect x="244" y="106" width="7" height="16"/>
      <rect x="256" y="103" width="7" height="16"/>
    </g>
    <polygon class="band-blue" points="5,170 160,138 160,150 5,182"/>
    <polygon class="band-cyan" points="5,190 265,138 265,160 5,210"/>
    <line class="line-gold" x1="5" y1="224" x2="50" y2="215"/>
    <line class="line-gold" x1="5" y1="230" x2="50" y2="221"/>
    <text class="t-perf-gold" font-size="15" transform="translate(52,222) rotate(-12)">HIGH-PERFORMANCE</text>
    <line class="line-gold" x1="210" y1="180" x2="265" y2="169"/>
    <line class="line-gold" x1="210" y1="186" x2="265" y2="175"/>
    <text class="t-tag" font-size="16" transform="translate(20,250) rotate(-12)">Synthetic Blend High Mileage</text>
    <rect class="art-area" x="75" y="258" width="110" height="44" rx="4" role="img" aria-label="Orange flame swoosh artwork"/>
    <g class="bar-blue">
      <rect x="95" y="335" width="5" height="18"/>
      <rect x="106" y="332" width="5" height="18"/>
      <rect x="117" y="329" width="5" height="18"/>
      <rect x="128" y="326" width="5" height="18"/>
      <rect x="139" y="323" width="5" height="18"/>
      <rect x="150" y="320" width="5" height="18"/>
      <rect x="161" y="317" width="5" height="18"/>
      <rect x="172" y="314" width="5" height="18"/>
      <rect x="183" y="311" width="5" height="18"/>
      <rect x="194" y="308" width="5" height="18"/>
    </g>
    <polygon class="band-blue" points="205,305 265,288 265,305 205,322"/>
    <rect class="grade-badge" x="3" y="342" width="88" height="30" rx="2"/>
    <text class="t-grade" font-size="23" x="8" y="366">10W40</text>
    <text class="t-volume" font-size="20" x="200" y="365">1Liters</text>
  </svg>

</main>
</body>
</html>
```